Real Estate Wordpress Landing Page

I'm looking to a landing page dedicated to my real estate brokerage that's catered to promoting that my company provides 1.5% listings to home sellers... I have a couple examples that I'm really looking towards mocking in a version with similar color schemes using my current company colors/website.

http://loftarco.com/
https://www.bluvane.com/about/one-percent-listing-fee

My brokerage company website is http://www.clearhaventa.us/

Target Market(s)

real estate home sellers & buyers

Industry/Entity Type

Real Estate

Coding

Coded - Design and coding required

Number of Pages Required

1 page

Colors
3176b5
0255a3
eaf1f7
cedeed

Requirements
Must have
• Company website colors - http://www.clearhaventa.us/
• Something around the lines of this website page - http://loftarco.com/
• Wordpress compatibility

```html
<!DOCTYPE html>
<html lang="en">
<head>
<meta charset="utf-8">
<title>Clearhaven Realty – List for 1.5% Commission</title>
<link href="https://fonts.googleapis.com/css2?family=Open+Sans:wght@400;600;700;800&display=swap" rel="stylesheet">
<style>
:root{
  --blue:#0255a3;
  --blue-mid:#3176b5;
  --blue-pale:#eaf1f7;
  --blue-soft:#cedeed;
  --ink:#222;
  --grey-band:#ebebeb;
  --card-grey:#e4e4e4;
  --panel:#2c2c2c;
  --footer:#1e1e1e;
  --white:#fff;
}
*{box-sizing:border-box;margin:0;padding:0}
html,body{width:1200px;height:3442px;overflow:hidden}
body{font-family:"Open Sans",Arial,sans-serif;color:var(--ink);background:var(--white);position:relative}
.abs{position:absolute}
.topnav{top:0;left:0;width:1200px;height:37px;background:var(--blue);display:flex;justify-content:center;z-index:2}
.topnav a{color:#fff;font-size:13px;line-height:37px;padding:0 15px;text-decoration:none}
.topnav a.active{background:rgba(0,0,0,.25)}
.hero{top:37px;left:0;width:1200px;height:578px;background:linear-gradient(180deg,#8fb6d6 0%,#c9dbe6 38%,#d9dcdc 55%,#6f8da3 80%,#3d5a70 100%)}
.btn-blue{background:var(--blue);color:#fff;font-size:13px;padding:0 12px;height:30px;line-height:30px;border-radius:2px;white-space:nowrap}
.logo-box{left:523px;top:39px;width:154px;height:151px;background:#fff;display:flex;flex-direction:column;align-items:center;justify-content:center;gap:8px}
.logo-box .sq{width:34px;height:34px;background:var(--blue)}
.logo-box span{font-size:19px;font-weight:700;color:var(--blue);text-align:center;line-height:1.15}
.hero-title{top:326px;left:0;width:1200px;text-align:center;color:#fff;font-size:56px;font-weight:800;letter-spacing:1px;text-shadow:0 2px 6px rgba(0,0,0,.35)}
.hero-sub{top:400px;left:0;width:1200px;text-align:center;color:#fff;font-size:22px;font-weight:800;text-shadow:0 2px 5px rgba(0,0,0,.35)}
.arrow-side{width:24px;height:34px;background:rgba(60,60,60,.55)}
.search{left:133px;top:560px;width:934px;height:156px;background:var(--panel);padding:14px 12px}
.search .row{display:flex;gap:10px;margin-bottom:10px}
.field{flex:1;height:38px;background:#fff;font-size:12px;color:#555;padding:0 12px;display:flex;align-items:center;justify-content:space-between}
.search .go{position:absolute;left:427px;top:111px;width:80px;height:32px;background:var(--blue);color:#fff;font-size:13px;text-align:center;line-height:32px}
.intro{top:790px;left:133px;width:934px;text-align:center}
.intro h3{color:var(--blue);font-size:23px;font-weight:800;margin-bottom:2px}
.intro h4{font-size:25px;font-weight:400;color:#333;margin-bottom:8px}
.intro p{font-size:12.5px;color:#333;line-height:1.6}
.band{left:0;width:1200px;background:var(--grey-band)}
.nav-arrow{color:#666;font-size:34px;font-weight:300}
.city-card{top:1058px;width:219px;height:225px;background:#fff;box-shadow:0 1px 3px rgba(0,0,0,.12)}
.city-card .ph{height:170px}
.city-card p{text-align:center;font-size:13px;color:#333;padding-top:12px;line-height:1.4}
.section-title{left:0;width:1200px;text-align:center;color:var(--blue);font-size:24px;font-weight:800}
.tab{top:1478px;height:41px;font-size:22px;font-weight:800;text-align:center;line-height:41px}
.prop-card{top:1556px;width:287px;height:250px;background:var(--card-grey)}
.prop-card .ph{height:158px}
.prop-card p{text-align:center;font-size:14px;color:#222;line-height:1.35;padding-top:14px}
.prop-card .price{color:var(--blue);font-size:19px;font-weight:700;padding-top:2px}
.vendor-strip{left:133px;top:2038px;width:934px;height:133px;background:#fff;display:flex}
.vendor-strip div{flex:1;border-right:1px solid #e4e4e4;display:flex;align-items:center;justify-content:center}
.vendor-strip div:last-child{border-right:none}
.badge{width:130px;height:26px;border-radius:3px}
.blog-card{top:2375px;width:443px;height:232px;background:#e6e6e6;display:flex}
.blog-card .ph{width:193px;height:232px}
.blog-card .body{padding:18px 20px;flex:1}
.blog-card h5{font-size:16px;font-weight:400;color:#333;line-height:1.3;margin-bottom:12px}
.blog-card p{font-size:10px;color:#666;line-height:1.6;margin-bottom:14px}
.blog-card .more{display:inline-block;border:1px solid #bbb;background:#fff;font-size:11px;color:#555;padding:5px 18px}
.view-all{left:557px;top:2632px;width:86px;height:36px;border:1px solid #bbb;background:#fff;font-size:11px;color:#555;text-align:center;line-height:34px}
.broker{left:133px;top:2749px;width:934px;height:299px;background:#e2e2e2}
.broker .ph{position:absolute;left:0;top:0;width:314px;height:299px;background:linear-gradient(180deg,#eef0f2,#c9cdd2)}
.broker .namebar{position:absolute;left:0;bottom:0;width:314px;height:42px;background:var(--blue);color:#fff;font-size:19px;font-weight:600;text-align:center;line-height:42px}
.broker .txt{position:absolute;left:342px;top:28px;width:570px}
.broker h6{font-size:27px;font-weight:400;color:var(--blue);margin-bottom:8px;white-space:nowrap}
.broker p{font-size:15px;color:#333;line-height:1.5;margin-bottom:18px}
.broker .call{font-size:20px;font-weight:700;color:#222}
.broker .phone{font-size:37px;font-weight:800;color:#111;display:flex;align-items:center;gap:10px;margin-top:2px}
.socials{display:flex;gap:7px;margin-top:14px}
.socials span{width:36px;height:36px;border:2px solid #444;border-radius:50%}
.footer{top:3126px;left:0;width:1200px;height:316px;background:var(--footer);color:#bbb}
.footer h6{font-size:16px;font-weight:400;color:#ddd;position:absolute;top:40px}
.footer .contact{position:absolute;left:133px;top:74px;font-size:10px;line-height:22px}
.footer .contact div{display:flex;align-items:center;gap:10px}
.footer .links{position:absolute;top:74px;font-size:10px;line-height:22px}
.footer .sub-note{position:absolute;left:823px;top:74px;font-size:10px}
.footer .email{position:absolute;left:823px;top:100px;width:244px;height:34px;background:#eee;color:#444;font-size:11px;padding:0 12px;display:flex;align-items:center;justify-content:space-between}
.footer .legal{position:absolute;left:133px;top:252px;font-size:9.5px;line-height:22px}
.footer .soc{position:absolute;left:978px;top:259px;display:flex;gap:18px}
.footer .soc span{width:14px;height:14px;background:#777;border-radius:2px}
</style>
</head>
<body>

<nav class="abs topnav">
  <a class="active">Home</a><a>Featured Cities</a><a>Property Search</a><a>Email Alerts</a><a>Communities</a><a>Buyers &amp; Sellers</a><a>Rentals</a><a>Investing</a><a>Contact</a><a>Clearhaven</a>
</nav>

<header class="abs hero" role="img" aria-label="Modern white beach house with pool at sunset"></header>
<div class="abs btn-blue" style="left:133px;top:54px">Buy With Us</div>
<div class="abs btn-blue" style="left:236px;top:54px">Sell With Us</div>
<div class="abs btn-blue" style="left:870px;top:54px">Email Us</div>
<div class="abs btn-blue" style="left:975px;top:54px">561-555-0193</div>
<div class="abs logo-box"><div class="sq"></div><span>Clearhaven<br>Realty</span></div>
<div class="abs arrow-side" style="left:0;top:308px"></div>
<div class="abs arrow-side" style="left:1176px;top:308px"></div>
<h1 class="abs hero-title">LIST FOR 1.5% COMMISSION,</h1>
<h2 class="abs hero-sub">AND RECEIVE TOP MARKETING FROM CLEARHAVEN REALTY!</h2>

<form class="abs search">
  <div class="row"><div class="field">Location<svg width="12" height="14" viewBox="0 0 12 14"><path d="M6 0a5 5 0 0 0-5 5c0 4 5 9 5 9s5-5 5-9a5 5 0 0 0-5-5z" fill="#333"/><circle cx="6" cy="5" r="2" fill="#fff"/></svg></div><div class="field">Property Type<svg width="10" height="6"><path d="M0 0h10L5 6z" fill="#333"/></svg></div><div class="field">Min. Price<b>$</b></div></div>
  <div class="row"><div class="field">Max. Price<b>$</b></div><div class="field">Beds<svg width="10" height="6"><path d="M0 0h10L5 6z" fill="#333"/></svg></div><div class="field">Baths<svg width="10" height="6"><path d="M0 0h10L5 6z" fill="#333"/></svg></div></div>
  <div class="go">SEARCH</div>
</form>

<section class="abs intro">
  <h3>BOYNTON BEACH REALTOR</h3>
  <h4>Discover Some of the Best Communities in Palm Beach County, FL</h4>
  <p>Over here at Clearhaven Realty, we have some of the best Realtors in the community who are ready to assist you and provide you with a free consultation. Give us a call today! 561-555-0193</p>
</section>

<section class="abs band" style="top:980px;height:385px"></section>
<div class="abs nav-arrow" style="left:54px;top:1148px">&#8249;</div>
<div class="abs nav-arrow" style="left:1128px;top:1148px">&#8250;</div>
<div class="abs city-card" style="left:133px"><div class="ph" role="img" aria-label="Mediterranean mansion in Boca Raton" style="background:linear-gradient(180deg,#8fb8dc,#c8b89a 60%,#6e8a4a)"></div><p>Boca Raton Homes for Sale</p></div>
<div class="abs city-card" style="left:372px"><div class="ph" role="img" aria-label="Palm-lined driveway in Jupiter" style="background:linear-gradient(180deg,#7fb0d8,#5f8a4f 55%,#b9b3a4)"></div><p>Jupiter Homes for Sale</p></div>
<div class="abs city-card" style="left:611px"><div class="ph" role="img" aria-label="Home with palm trees in Palm Springs" style="background:linear-gradient(180deg,#9cc3e2,#6f934a 50%,#d4c8b0)"></div><p>Palm Springs Homes for Sale</p></div>
<div class="abs city-card" style="left:849px"><div class="ph" role="img" aria-label="Large estate home in Boynton Beach" style="background:linear-gradient(180deg,#a9c9e6,#b9b3a0 55%,#4f7a3a)"></div><p>Boynton Beach Homes for Sale</p></div>

<h3 class="abs section-title" style="top:1438px">LATEST PROPERTIES WE'VE...</h3>
<div class="abs tab" style="left:477px;width:119px;background:var(--blue);color:#fff">SOLD</div>
<div class="abs tab" style="left:604px;width:119px;background:#cfcfcf;color:#888">RENTED</div>
<div class="abs nav-arrow" style="left:54px;top:1655px">&#8249;</div>
<div class="abs nav-arrow" style="left:1128px;top:1655px">&#8250;</div>
<div class="abs prop-card" style="left:133px"><div class="ph" role="img" aria-label="Two-storey house with garage" style="background:linear-gradient(180deg,#6d9a56,#d8d2c2 55%,#8a8a84)"></div><p>4218 Maple Hollow Lane<br>Lakeview, FL 33401</p><p class="price">$325,000</p></div>
<div class="abs prop-card" style="left:457px"><div class="ph" role="img" aria-label="Condo living room interior" style="background:linear-gradient(180deg,#d6d6d4,#7c7a78 60%,#3e3e3e)"></div><p>310 Seabreeze Avenue, 104<br>Boynton Beach, FL 33400</p><p class="price">$485,000</p></div>
<div class="abs prop-card" style="left:780px"><div class="ph" role="img" aria-label="Townhouse with palms and garage" style="background:linear-gradient(180deg,#8dbbe0,#d9cdb4 55%,#7a8c68)"></div><p>8712 Willow Brook Circle<br>Lakeview, FL 33402</p><p class="price">$325,000</p></div>

<section class="abs band" style="top:1886px;height:368px"></section>
<h3 class="abs section-title" style="top:1960px">OUR VENDORS</h3>
<p class="abs" style="left:0;top:1996px;width:1200px;text-align:center;font-size:16px;color:#333">We work with a few of the most exceptional companies to service each real estate transaction.</p>
<div class="abs nav-arrow" style="left:54px;top:2078px">&#8249;</div>
<div class="abs nav-arrow" style="left:1128px;top:2078px">&#8250;</div>
<div class="abs vendor-strip">
  <div><span class="badge" style="background:#c5d6b4"></span></div>
  <div><span class="badge" style="background:#b4c8e0"></span></div>
  <div><span class="badge" style="background:#c3cbe0"></span></div>
  <div><span class="badge" style="background:#2a3f86"></span></div>
</div>

<h3 class="abs section-title" style="top:2328px">BLOG</h3>
<article class="abs blog-card" style="left:133px"><div class="ph" role="img" aria-label="Modern apartment building" style="background:linear-gradient(180deg,#8fb4d6,#a88a6a 50%,#5a4a3a)"></div><div class="body"><h5>Etiam mattis augue vehicula odio posuere, sit amet</h5><p>Etiam mattis augue vehicula odio posuere, sit amet tempus lectus luctus. Nulla facilisi. Etiam vel massa elementum, bibendum tellus venenatis, feugiat massa.</p><span class="more">Read More</span></div></article>
<article class="abs blog-card" style="left:624px"><div class="ph" role="img" aria-label="Hand holding a floor plan on a tablet" style="background:linear-gradient(135deg,#c9d8e4,#8fa6b8 60%,#d9c6b4)"></div><div class="body"><h5>Curabitur venenatis lacinia ornare. Cras sollicitudin</h5><p>Etiam mattis augue vehicula odio posuere, sit amet tempus lectus luctus. Nulla facilisi. Etiam vel massa elementum, bibendum tellus venenatis, feugiat massa.</p><span class="more">Read More</span></div></article>
<div class="abs view-all">View All</div>

<section class="abs broker">
  <div class="ph" role="img" aria-label="Portrait of the broker in a suit"></div>
  <div class="namebar">Marcus Delacroix</div>
  <div class="txt">
    <h6>MARCUS DELACROIX, Lic. Real Estate Broker</h6>
    <p>On average, our customers save $5,600 when they list with us... and they still receive top marketing and quality professional service!</p>
    <div class="call">CALL US TODAY AND SAVE THOUSANDS $$$</div>
    <div class="phone"><svg width="28" height="28" viewBox="0 0 24 24"><path d="M6.6 10.8a15 15 0 0 0 6.6 6.6l2.2-2.2a1 1 0 0 1 1-.25 11.4 11.4 0 0 0 3.6.6 1 1 0 0 1 1 1V20a1 1 0 0 1-1 1A17 17 0 0 1 3 4a1 1 0 0 1 1-1h3.5a1 1 0 0 1 1 1c0 1.25.2 2.45.6 3.6a1 1 0 0 1-.25 1z" fill="#111"/></svg>561-555-0147</div>
    <div class="socials"><span></span><span></span><span></span><span></span><span></span><span></span></div>
  </div>
</section>

<footer class="abs footer">
  <h6 style="left:133px">Contact</h6>
  <div class="contact">
    <div><svg width="9" height="11" viewBox="0 0 12 14"><path d="M6 0a5 5 0 0 0-5 5c0 4 5 9 5 9s5-5 5-9a5 5 0 0 0-5-5z" fill="#aaa"/></svg>2400 Harbor Point Blvd, Ste 310, Boynton Beach, FL 33426</div>
    <div><svg width="9" height="9" viewBox="0 0 24 24"><path d="M6.6 10.8a15 15 0 0 0 6.6 6.6l2.2-2.2 5.6 1.4V21A17 17 0 0 1 3 3h4.4l1.4 5.6z" fill="#aaa"/></svg>561-555-0193</div>
    <div><svg width="9" height="9"><rect width="9" height="9" fill="#aaa"/></svg>561-555-0182</div>
    <div><svg width="10" height="8"><rect width="10" height="8" fill="#aaa"/><path d="M0 0l5 4 5-4" stroke="#1e1e1e" fill="none"/></svg>contact@clearhaventa.us</div>
  </div>
  <h6 style="left:531px">Links</h6>
  <div class="links" style="left:531px">Home<br>Featured Cities<br>Property Search<br>Email Alerts<br>Communities</div>
  <div class="links" style="left:635px">Buyers &amp; Sellers<br>Rentals<br>Investing<br>Contact<br>Clearhaven</div>
  <h6 style="left:823px">SUBSCRIBE TO THE NEWSLETTER</h6>
  <div class="sub-note">Subscribe to Newsletter</div>
  <div class="email">Email Address<svg width="14" height="11"><rect width="14" height="11" fill="#333"/><path d="M0 0l7 5 7-5" stroke="#eee" fill="none"/></svg></div>
  <div class="legal">Copyright © 2018 Clearhaven Realty. All rights reserved.<br>Privacy Terms and Conditions Contact Us Mobile Notary</div>
  <div class="soc"><span></span><span></span><span></span></div>
</footer>

</body>
</html>
```